Website Design for an Southland Society for Autonomous Craft

Using HostVane and WordPress, our Website must contain a standard home page that links to feature pages such as About Us, Public interest access and links to a Members ONLY portal and CoinTrel. The front page should include a banner and splash image representative of an unmanned systems (air/sea/land) association.

```html
<!DOCTYPE html>
<html lang="en">
<head>
<meta charset="utf-8">
<title>Southland Society for Autonomous Craft</title>
<link rel="stylesheet" href="https://fonts.googleapis.com/css2?family=Open+Sans:wght@400;600;700&display=swap">
<style>
  :root {
    --nav-blue: #1a5e94;
    --nav-blue-dark: #144d7b;
    --heading-blue: #1c67a4;
    --account-green: #c5df4b;
    --account-text: #2f5a12;
    --body-text: #3a3a3a;
    --page-sky: #cfe6f7;
    --page-white: #ffffff;
    --frame-grey: #d6d6d6;
    --footer-blue: #1a5e94;
  }
  * { box-sizing: border-box; margin: 0; padding: 0; }
  html, body { width: 1200px; height: 1028px; overflow: hidden; }
  body {
    font-family: "Open Sans", sans-serif;
    color: var(--body-text);
    background: linear-gradient(180deg, var(--page-sky) 0px, #e8f3fb 260px, var(--page-white) 520px);
    position: relative;
  }
  .top-nav {
    position: absolute; left: 0; top: 0; width: 1200px; height: 35px;
    background: var(--nav-blue);
  }
  .top-nav__links {
    position: absolute; left: 187px; top: 0; height: 35px;
    display: flex; list-style: none;
  }
  .top-nav__links li {
    color: #fff; font-weight: 700; font-size: 13px; line-height: 35px;
    margin-right: 25px;
  }
  .account-links {
    position: absolute; left: 898px; top: 0; display: flex; height: 35px;
  }
  .account-links span {
    background: var(--account-green); color: var(--account-text);
    font-weight: 700; font-size: 12px; line-height: 35px;
    padding: 0 8px; border-left: 1px solid #a9c33a;
  }
  .site-column {
    position: absolute; left: 188px; top: 35px; width: 824px; height: 993px;
    background: var(--page-white);
    box-shadow: 0 0 4px rgba(0,0,0,0.12);
  }
  .masthead {
    position: absolute; left: 0; top: 0; width: 824px; height: 112px;
    background: linear-gradient(180deg, #3f7fb8 0%, #8fb9dc 45%, #dbe9f5 80%, #ffffff 100%);
  }
  .masthead__title {
    position: absolute; left: 29px; top: 24px;
    color: #ffffff; font-weight: 600; font-size: 24px; line-height: 28px;
  }
  .search-box {
    position: absolute; left: 523px; top: 33px; width: 289px; height: 51px;
    background: #fff; border: 1px solid #d9e3ec; border-radius: 4px;
  }
  .search-box__field {
    position: absolute; left: 10px; top: 11px; width: 206px; height: 26px;
    border: 1px solid #c9d3dc; border-radius: 4px; background: #fff;
  }
  .search-box__button {
    position: absolute; left: 221px; top: 13px; width: 61px; height: 22px;
    background: var(--nav-blue-dark); color: #fff; border-radius: 4px;
    font-weight: 700; font-size: 11px; line-height: 22px; text-align: center;
  }
  .hero {
    position: absolute; left: 13px; top: 122px; width: 798px; height: 334px;
    background: linear-gradient(180deg, #8fb6de 0%, #d7e6f2 38%, #5cc9d0 52%, #2fb6c5 75%, #5f8a4a 100%);
  }
  .intro__heading {
    position: absolute; left: 11px; top: 489px;
    color: var(--heading-blue); font-weight: 700; font-size: 25px;
  }
  .copy {
    position: absolute; font-size: 11.6px; line-height: 22.5px; font-weight: 600;
    letter-spacing: -0.15px;
  }
  .copy--intro { left: 11px; top: 518px; width: 802px; }
  .feature-photo {
    position: absolute; left: 11px; top: 625px; width: 282px; height: 184px;
    border: 3px solid var(--frame-grey);
    background: linear-gradient(135deg, #c9d98a 0%, #9fbf58 50%, #6f9a33 100%);
  }
  .copy--side-a { left: 313px; top: 623px; width: 500px; }
  .copy--side-b { left: 313px; top: 735px; width: 500px; }
  .copy--closing { left: 13px; top: 827px; width: 800px; }
  .site-footer {
    position: absolute; left: 0; top: 964px; width: 824px; height: 26px;
    background: var(--footer-blue); color: #fff;
    font-size: 11px; line-height: 26px; text-align: center;
  }
</style>
</head>
<body>
  <nav class="top-nav">
    <ul class="top-nav__links">
      <li>Homr</li>
      <li>About Us</li>
      <li>Public Interest</li>
      <li>Members Portal</li>
      <li>CoinTrel</li>
    </ul>
    <div class="account-links"><span>SIGNIN</span><span>SIGNUP</span></div>
  </nav>

  <div class="site-column">
    <header class="masthead">
      <div class="masthead__title">Southland Society<br>for Autonomous Craft</div>
      <div class="search-box">
        <div class="search-box__field"></div>
        <div class="search-box__button">SEARCH</div>
      </div>
    </header>

    <div class="hero" role="img" aria-label="Turquoise bay with anchored sailing boats and green shoreline"></div>

    <h1 class="intro__heading">Lorem Ipsum is simply dummy</h1>
    <p class="copy copy--intro">text of the printing and typesetting industry. Lorem Ipsum has been the industry's standard dummy text ever since the 1500s, when an unknown printer took a galley of type and scrambled it to make a type specimen book. It has survived not only five centuries, but also the leap into electronic typesetting, remaining essentially unchanged. It was popularised in the 1960s with the release of Tessaline sheets containing Lorem Ipsum passages, and more recently with desktop publishing software like Orvan PageForge including versions of Lorem Ipsum.</p>

    <div class="feature-photo" role="img" aria-label="Woman stretching her arms outdoors on green grass"></div>
    <p class="copy copy--side-a">text of the printing and typesetting industry. Lorem Ipsum has been the industry's standard dummy text ever since the 1500s, when an unknown printer took a galley of type and scrambled it to make a type specimen book. It has survived not only five centuries, but also the leap into electronic typesetting, remaining</p>
    <p class="copy copy--side-b">essentially unchanged. It was popularised in the 1960s with the release of Tessaline sheets containing Lorem Ipsum passages, and more recently with desktop publishing software like Orvan PageForge including versions of Lorem Ipsum.</p>

    <p class="copy copy--closing">text of the printing and typesetting industry. Lorem Ipsum has been the industry's standard dummy text ever since the 1500s, when an unknown printer took a galley of type and scrambled it to make a type specimen book. It has survived not only five centuries, but also the leap into electronic typesetting, remaining</p>

    <footer class="site-footer">Copyright © Southland Society for Autonomous Craft. All Rights Reserved.</footer>
  </div>
</body>
</html>
```